Harbor Crest Renewal Business Cards

We need a sleek and sexy business card design

Contact Information for Business Card

Name, address, phone number, email. Martin DeSolva 482 Bramble Court Suite 200C Wrenford NY 11790 (631)584-2276 Also a second version with the name Derek Hollis

```html
<!DOCTYPE html>
<html lang="en">
<head>
<meta charset="utf-8">
<title>Harbor Crest Renewal Business Cards</title>
<link href="https://fonts.googleapis.com/css2?family=Montserrat:wght@500;700&display=swap" rel="stylesheet">
<style>
  :root {
    --bg: #e4e6e7;
    --card: #ffffff;
    --red: #d5442a;
    --blue: #1f4a92;
    --ink: #1e1e1e;
  }
  * { margin: 0; padding: 0; box-sizing: border-box; }
  html, body { width: 1200px; height: 928px; overflow: hidden; }
  body {
    position: relative;
    background: var(--bg);
    font-family: "Montserrat", sans-serif;
    color: var(--ink);
  }
  .card {
    position: absolute;
    background: var(--card);
    box-shadow: 0 6px 18px rgba(0,0,0,0.18);
  }
  .card-front { left: 267px; top: 58px; width: 670px; height: 382px; }
  .card-back  { left: 263px; top: 483px; width: 677px; height: 387px; }

  .brand {
    position: absolute;
    left: 0; right: 0; top: 166px;
    display: flex; align-items: center; justify-content: center; gap: 14px;
  }
  .brand-mark {
    flex: none;
    width: 26px; height: 26px; border-radius: 50%;
    background: var(--red);
  }
  .brand-name {
    font-weight: 700; font-size: 40px; color: var(--blue);
    letter-spacing: 0.5px; white-space: nowrap;
  }

  .person {
    position: absolute; right: 360px; top: 168px; text-align: right;
  }
  .person-name { font-weight: 700; font-size: 27px; letter-spacing: 0.3px; line-height: 1; white-space: nowrap; }
  .person-name .first { color: var(--red); }
  .person-name .last { color: var(--blue); }
  .person-role { font-weight: 500; font-size: 16px; margin-top: 12px; padding-right: 8px; letter-spacing: 0.5px; }

  .contacts {
    position: absolute; left: 354px; top: 156px;
    list-style: none;
  }
  .contacts li {
    display: flex; align-items: center; gap: 10px;
    font-size: 16px; font-weight: 500; letter-spacing: 0.5px;
    height: 24.5px; white-space: nowrap;
  }
  .contacts svg { width: 12px; height: 12px; flex: none; }

  .footer {
    position: absolute; left: 54px; top: 324px;
    display: flex; align-items: center; gap: 14px;
    white-space: nowrap;
  }
  .footer-brand {
    display: flex; align-items: center; gap: 5px;
    font-weight: 700; font-size: 9.5px; color: var(--blue);
  }
  .footer-brand .brand-mark { width: 9px; height: 9px; }
  .address { font-size: 16px; font-weight: 500; letter-spacing: 0.5px; }
</style>
</head>
<body>
  <section class="card card-front">
    <div class="brand">
      <span class="brand-mark"></span>
      <span class="brand-name">Harbor Crest Renewal</span>
    </div>
  </section>

  <section class="card card-back">
    <div class="person">
      <div class="person-name"><span class="first">DEREK</span> <span class="last">HOLLIS</span></div>
      <div class="person-role">Director</div>
    </div>

    <ul class="contacts">
      <li>
        <svg viewBox="0 0 12 12" aria-hidden="true"><path d="M2.5 1 L4.5 1 L5 3.5 L3.8 4.3 Q4.8 6.8 7.7 8.2 L8.5 7 L11 7.5 L11 9.5 Q10.5 11 9 11 Q1 10 1 2.5 Q1.2 1 2.5 1Z" fill="var(--red)"/></svg>
        (631)584-2276
      </li>
      <li>
        <svg viewBox="0 0 12 12" aria-hidden="true"><rect x="0.5" y="2.5" width="11" height="7.5" rx="1" fill="var(--red)"/><path d="M1 3 L6 6.8 L11 3" stroke="#fff" stroke-width="1" fill="none"/></svg>
        info@harborcrestrn.com
      </li>
      <li>
        <svg viewBox="0 0 12 12" aria-hidden="true" fill="none" stroke="var(--red)" stroke-width="0.9"><circle cx="6" cy="6" r="5.2"/><ellipse cx="6" cy="6" rx="2.3" ry="5.2"/><path d="M0.8 6 H11.2 M1.6 3.5 H10.4 M1.6 8.5 H10.4"/></svg>
        www.harborcrestrn.com
      </li>
    </ul>

    <div class="footer">
      <div class="footer-brand"><span class="brand-mark"></span>Harbor Crest Renewal</div>
      <div class="address">482 Bramble Court, Suite 200C, Wrenford NY 11790</div>
    </div>
  </section>
</body>
</html>
```